Business Card and Letterhead for Vantage Psychology

We need a business card design and letterhead to use for our Psychology firm that specializes in psychoeducational assessments and individual therapy. Our motto is Purpose-Driven Assessments, Meaning-Centered Therapy.Our contact information is as follows:
Vantage Psychology
The Marwick Block - 6127-48St.
Box 2716 Olds, AB
T2K 3M8
t 403.555.0148 (VANT)
f 403.555.0172
www.vantagepsychology-example.ca
The business card will be used for two different psychologists so I can supply names nearer to completion. We prefer clean, uncluttered looks.

Target Market(s)

Clients, Educators

Font styles to use
Sans Serif

Colors

Designer to choose colors to be used in the design.

Requirements
Must have
• All relevant contact info, logo, some "white" space.
Nice to have
• It would be nice to see letterhead options that have the logo on the top of the page but also options that have it on the side. I think top of the page is probably our preference.
Should not have
• Too much clutter!

```html
<!DOCTYPE html>
<html lang="en">
<head>
<meta charset="utf-8">
<title>Vantage Psychology – Stationery</title>
<link href="https://fonts.googleapis.com/css2?family=Lato:wght@400;700&display=swap" rel="stylesheet">
<style>
  :root{
    --bg:#a3a3a3;
    --paper:#ffffff;
    --blue:#65bddd;
    --orange:#f5a742;
    --ink:#2b2b2b;
    --faint:#f1f1f1;
    --window:#ececec;
  }
  *{box-sizing:border-box;margin:0;padding:0}
  html,body{width:1200px;height:958px;overflow:hidden}
  body{background:var(--bg);font-family:'Lato',sans-serif;color:var(--ink);position:relative}
  .piece{position:absolute;background:var(--paper);overflow:hidden}
  .mark{position:absolute;border-radius:50%;background:var(--blue)}
  .brand{position:absolute;font-family:'Lato',sans-serif;font-weight:700;letter-spacing:.5px;color:var(--blue);white-space:nowrap;text-transform:uppercase}
  .url{position:absolute;font-size:5.5px;color:#555;white-space:nowrap}
  .footer-wave{position:absolute;left:0;bottom:0;width:100%}
  .footer-url{position:absolute;color:#fff;white-space:nowrap}

  /* business cards */
  .card{top:38px;width:211px;height:121px}
  .card--white{left:47px}
  .card--blue-a{left:341px;background:var(--blue)}
  .card--blue-b{left:634px;background:var(--blue)}
  .card--contact{left:928px}
  .card .centered{left:0;width:100%;text-align:center}
  .card--blue-a .mark,.card--blue-b .mark{background:#fff;border:3px solid rgba(255,255,255,.6)}
  .card--blue-a .brand,.card--blue-b .brand{color:#fff}
  .card--blue-a .url,.card--blue-b .url{color:#fff}

  .person{position:absolute;right:12px;text-align:right}
  .person .name{font-size:8.5px;color:var(--blue)}
  .person .title{font-size:5.5px;color:#444;margin-top:1px}
  .rule{position:absolute;left:13px;right:12px;top:71px;height:1px;background:var(--blue)}
  .contact-list{position:absolute;left:13px;top:82px;font-size:5.3px;line-height:7px;list-style:none}
  .contact-list li{display:flex;align-items:center;gap:3px}
  .dot-icon{width:4px;height:4px;border-radius:50%;background:var(--blue);display:inline-block}
  .address-right{position:absolute;right:12px;top:82px;font-size:5.3px;line-height:7px;text-align:right}

  /* letterhead */
  .letterhead{left:45px;top:196px;width:501px;height:708px;border-top:3px solid var(--blue)}
  .letterhead .divider{position:absolute;left:359px;top:40px;width:1px;height:56px;background:#777}
  .letterhead .address{position:absolute;left:370px;top:42px;font-size:7.3px;line-height:9.2px}
  .letterhead .address .icon-row{display:flex;align-items:center;gap:5px}
  .letterhead .address svg{flex:none}
  .body-copy{position:absolute;left:40px;top:204px;width:370px;font-size:7.3px;line-height:11.8px;letter-spacing:.1px}
  .body-copy p{margin-bottom:11.8px}
  .signature{position:absolute;left:45px;top:425px;width:130px;height:24px;background:linear-gradient(90deg,#e6e6e6,#f4f4f4);border-radius:3px}
  .watermark{position:absolute;border-radius:50%;background:var(--faint)}

  /* envelopes */
  .envelope-back{left:615px;top:294px;width:524px;height:262px}
  .flap{position:absolute;left:0;top:0;width:100%;height:78px}
  .envelope-back .mark{background:#fff}
  .return-line{position:absolute;left:0;width:100%;top:236px;text-align:center;font-size:5.5px;color:#333}
  .return-line .sep{color:var(--blue)}
  .envelope-front{left:615px;top:642px;width:524px;height:262px}
  .address-window{position:absolute;left:35px;top:118px;width:207px;height:90px;background:var(--window);border:1px solid #d6d6d6;border-radius:4px}
</style>
</head>
<body>

<!-- Card: white front -->
<section class="piece card card--white">
  <div class="mark" style="left:86px;top:37px;width:40px;height:40px"></div>
  <div class="brand centered" style="top:81px;font-size:10px">Vantage Psychology</div>
  <div class="url centered" style="top:102px">www.vantagepsychology-example.ca</div>
</section>

<!-- Card: blue front A -->
<section class="piece card card--blue-a">
  <div class="mark" style="left:86px;top:38px;width:40px;height:40px"></div>
  <div class="brand centered" style="top:83px;font-size:10px">Vantage Psychology</div>
  <div class="url centered" style="top:105px">www.vantagepsychology-example.ca</div>
</section>

<!-- Card: blue front B -->
<section class="piece card card--blue-b">
  <div class="mark" style="left:86px;top:38px;width:40px;height:40px"></div>
  <div class="brand centered" style="top:83px;font-size:10px">Vantage Psychology</div>
  <div class="url centered" style="top:105px">www.vantagepsychology-example.ca</div>
</section>

<!-- Card: contact back -->
<section class="piece card card--contact">
  <div class="mark" style="left:52px;top:25px;width:27px;height:27px"></div>
  <div class="brand" style="left:13px;top:55px;font-size:7.5px">Vantage Psychology</div>
  <div class="person" style="top:51px">
    <div class="name">Dana Whitlock</div>
    <div class="title">Psychologist</div>
  </div>
  <div class="rule"></div>
  <ul class="contact-list">
    <li><span class="dot-icon"></span>403.555.0148 (VANT)</li>
    <li><span class="dot-icon"></span>403.555.0172</li>
    <li><span class="dot-icon"></span>info@vantagepsychology-example.ca</li>
  </ul>
  <div class="address-right">Vantage Psychology<br>The Marwick Block - 6127-48St.<br>Box 2716 Olds, AB, T2K 3M8</div>
  <svg class="footer-wave" width="211" height="14" viewBox="0 0 500 40" preserveAspectRatio="none">
    <path d="M0 40 C140 16 300 6 420 4 C300 12 150 24 30 40 Z" fill="var(--orange)"/>
    <path d="M0 40 C160 22 320 14 500 12 L500 40 Z" fill="var(--blue)"/>
  </svg>
  <div class="footer-url" style="right:12px;bottom:2px;font-size:5px">www.vantagepsychology-example.ca</div>
</section>

<!-- Letterhead -->
<section class="piece letterhead">
  <div class="mark" style="left:98px;top:35px;width:58px;height:58px"></div>
  <div class="brand" style="left:42px;top:97px;font-size:14px">Vantage Psychology</div>

  <div class="divider"></div>
  <div class="address">
    Vantage Psychology<br>
    The Marwick Block - 6127-48St.<br>
    Box 2716 Olds, AB, T2K 3M8
    <div class="icon-row" style="margin-top:3px">
      <svg width="6" height="6" viewBox="0 0 10 10"><path d="M2 1 L4 1 L5 3.5 L3.8 4.6 C4.5 6 5.5 7 6.8 7.6 L8 6.4 L10 7.4 L10 9.5 C5 10 0 5 0.5 1 Z" fill="var(--blue)"/></svg>403.555.0148 (VANT)
    </div>
    <div class="icon-row">
      <svg width="6" height="6" viewBox="0 0 10 10"><rect x="1" y="3" width="8" height="5" fill="var(--blue)"/><rect x="3" y="0.5" width="4" height="3" fill="var(--blue)"/></svg>403.555.0172
    </div>
    <div class="icon-row">
      <svg width="6" height="6" viewBox="0 0 10 10"><rect x="0.5" y="2" width="9" height="6" fill="var(--blue)"/><path d="M0.5 2 L5 5.5 L9.5 2" stroke="#fff" fill="none"/></svg>info@vantagepsychology-example.ca
    </div>
  </div>

  <div class="body-copy">
    <p>Lorem ipsum dolor sit amet, consectetur adipiscing elit. Praesent non est diam. Vivamus risus sem, gravida sit amet nibh ut, ornare lobortis ante. Aliquam sollicitudin, mauris tincidunt semper venenatis, orci est pretium augue, ut vestibulum felis velit bibendum urna. Integer sollicitudin aliquet ligula, non ultricies nisl efficitur nec. Aliquam felis lorem, facilisis ac condimentum quis, consectetur volutpat lacus. Proin fermentum sem quis elit efficitur, eu tempus magna maximus.</p>
    <p>Aenean a mi tortor. Morbi pretium mi sed cursus vehicula. Lorem ipsum dolor sit amet, consectetur adipiscing elit. In finibus eros ac maximus finibus. Nunc pretium pellentesque tellus. Nullam accumsan nisl non diam camodo sagittis. Nunc et ante sit amet urna auctor convallis. Maecenas sed fringilla metus, sit amet vulputate felis. Morbi eget tempor nisi. Aliquam erat volutpat. Aenean laoreet interdum tempus.</p>
    <p>Maecenas dignissim placerat mauris, vitae sollicitudin ex. Integer bibendum maximus mauris, ac tempor urna viverra id. Integer tincidunt lobortis nisl at posuere. Sed faucibus vulputate finibus. Maecenas convallis, sem quis pellentesque cursus, urna quam aliquam augue, quis porttitor eros est nec lectus. Sed mattis at tellus ut blandit. Aenean nunc magna, viverra sed mauris vel, porta finibus lacus. Nullam bibendum turpis rutrum porta placerat</p>
  </div>
  <div class="signature" role="img" aria-label="Handwritten signature of the sender"></div>

  <div class="watermark" style="left:117px;top:507px;width:144px;height:144px"></div>

  <svg class="footer-wave" width="501" height="46" viewBox="0 0 500 40" preserveAspectRatio="none">
    <path d="M0 40 C140 18 300 6 370 5 C280 10 140 24 20 40 Z" fill="var(--orange)"/>
    <path d="M0 40 C160 24 330 16 500 12 L500 40 Z" fill="var(--blue)"/>
  </svg>
  <div class="footer-url" style="right:28px;bottom:10px;font-size:8px">www.vantagepsychology-example.ca</div>
</section>

<!-- Envelope: back -->
<section class="piece envelope-back">
  <svg class="flap" viewBox="0 0 524 78" preserveAspectRatio="none">
    <path d="M0 0 L524 0 L504 70 Q501 78 492 78 L32 78 Q23 78 20 70 Z" fill="var(--blue)"/>
  </svg>
  <div class="mark" style="left:248px;top:24px;width:30px;height:30px"></div>
  <div class="return-line">Vantage Psychology <span class="sep">•</span> The Marwick Block - 6127-48St. <span class="sep">•</span> Box 2716 Olds <span class="sep">•</span> AB, T2K 3M8</div>
</section>

<!-- Envelope: front -->
<section class="piece envelope-front">
  <div class="mark" style="left:91px;top:38px;width:46px;height:46px"></div>
  <div class="brand" style="left:35px;top:87px;font-size:12.5px">Vantage Psychology</div>
  <div class="address-window"></div>
  <div class="watermark" style="left:318px;top:79px;width:124px;height:124px"></div>
  <svg class="footer-wave" width="524" height="34" viewBox="0 0 500 40" preserveAspectRatio="none">
    <path d="M0 40 C140 18 300 6 400 4 C290 10 140 24 20 40 Z" fill="var(--orange)"/>
    <path d="M0 40 C160 26 330 18 500 12 L500 40 Z" fill="var(--blue)"/>
  </svg>
  <div class="footer-url" style="right:16px;bottom:8px;font-size:8px">www.vantagepsychology-example.ca</div>
</section>

</body>
</html>
```